Patent Law

Need to develop a home page for a patent lawyer.

Colors should go with logo, blues...

Company Name- Velric Dunmore, PLLC

Company Overview-

I am an Intellectual Property Lawyer and focus on patents, copyrights, trademarks, & trade secrets. I work with small businesses and start ups in the chemical and biotech industries.

Why Us-

I am small firm that can provide large-firm service at a reasonable price. I also can charge flat-fees for entreprenuers in certain practice areas.

Services-
Intellectual Property
Patents
Copyrights
Trademarks
Trade secrets
Healthcare Compliance
Elder law
Wills
Trusts

Website we like-
http://www.tolvanecrest.com/ - within industry!!
http://www.quarnhollet.com/
http://brevicktallon.com/
http://thegravelwrights.com/

Target Market(s)

My customers will be small business, specifically small start-up companies in the chemical and biotech arena.

Industry/Entity Type

Trade

Requirements
Must have
• Colors should go with logo, blues...

```html
<!DOCTYPE html>
<html lang="en">
<head>
<meta charset="utf-8">
<title>Velric Dunmore, PLLC – Patent Law</title>
<link rel="stylesheet" href="https://fonts.googleapis.com/css2?family=Montserrat:wght@400;600;700&family=Open+Sans:ital,wght@0,300;0,400;0,600;1,400&display=swap">
<style>
  :root {
    --header-bg: #edefe2;
    --page-bg: #f3f3f3;
    --ink: #1b1b1b;
    --text: #555555;
    --muted: #8a8a8a;
    --blue: #1e8fd6;
    --blue-deep: #3a4fa8;
    --navy: #2c3e8f;
    --rule: #dcdcdc;
    --badge: #c4c4c4;
    --btn-dark: #4a4f55;
  }
  * { box-sizing: border-box; margin: 0; padding: 0; }
  html, body { width: 1010px; height: 1200px; overflow: hidden; }
  body { position: relative; background: var(--page-bg); font-family: "Open Sans", sans-serif; color: var(--text); }
  .abs { position: absolute; }

  /* header */
  .site-header { position: absolute; left: 0; top: 0; width: 1010px; height: 84px; background: var(--header-bg); }
  .brand { left: 202px; top: 18px; display: flex; flex-direction: column; align-items: center; width: 108px; }
  .brand-dot { width: 34px; height: 34px; border-radius: 50%; background: var(--blue-deep); margin-bottom: 8px; }
  .brand-name { font-family: "Open Sans", sans-serif; font-size: 10.5px; font-weight: 600; color: var(--ink); letter-spacing: .4px; white-space: nowrap; text-transform: uppercase; }
  .main-nav { left: 353px; top: 62px; display: flex; gap: 0; font-size: 9px; color: #555; }
  .main-nav a { text-decoration: none; color: inherit; position: absolute; white-space: nowrap; }
  .main-nav .is-active { color: var(--blue); border-bottom: 2px solid var(--blue); padding-bottom: 3px; }
  .call-box { right: 223px; top: 8px; text-align: right; line-height: 1.1; }
  .call-box .q { font-size: 10.5px; color: #666; }
  .call-box .p { font-size: 8px; color: #777; }
  .call-box .phone { font-family: "Montserrat", sans-serif; font-weight: 700; font-size: 15px; color: var(--navy); margin-top: 1px; }
  .or { left: 687px; top: 58px; font-size: 8.5px; color: #999; }
  .email-btn { left: 714px; top: 54px; width: 73px; height: 20px; background: var(--btn-dark); border-radius: 2px; color: #fff; font-size: 8.5px; display: flex; align-items: center; justify-content: center; gap: 5px; }

  /* hero */
  .hero { position: absolute; left: 0; top: 84px; width: 1010px; height: 305px;
    background: radial-gradient(ellipse 200px 190px at 300px 170px, #c99a4e 0%, #8c5a26 45%, transparent 80%),
                linear-gradient(90deg, #5e3618 0%, #7a4a22 30%, #a26a35 55%, #7d4f28 80%, #5a3a1e 100%); }
  .hero-title { left: 468px; top: 160px; font-family: "Montserrat", sans-serif; font-weight: 700; font-size: 33px; color: #fff; }
  .hero-sub { left: 468px; top: 196px; font-family: "Open Sans", sans-serif; font-weight: 300; font-size: 23px; color: #fff; }
  .hero-text { left: 468px; top: 235px; width: 290px; font-size: 8.6px; line-height: 11.5px; color: #fff; }
  .contact-btn { left: 469px; top: 316px; width: 167px; height: 43px; background: linear-gradient(90deg, var(--blue-deep), var(--blue)); color: #fff; padding: 8px 0 0 13px; }
  .contact-btn small { display: block; font-size: 8.5px; }
  .contact-btn strong { display: block; font-weight: 400; font-size: 17px; line-height: 1.1; }
  .contact-btn svg { position: absolute; right: 15px; top: 12px; }

  /* info columns */
  .info-col { top: 422px; width: 170px; }
  .info-col h3 { font-family: "Montserrat", sans-serif; font-weight: 600; font-size: 11.5px; color: var(--ink); }
  .info-col .lead { font-style: italic; font-size: 8.5px; color: var(--muted); margin: 1px 0 9px; }
  .info-col p { font-size: 6.8px; line-height: 11px; color: #555; }
  .info-col .sep { margin: 0 4px; }
  .rule { position: absolute; left: 197px; width: 616px; height: 1px; background: var(--rule); }

  /* about */
  .avatar { left: 410px; top: 580px; width: 68px; height: 68px; border-radius: 50%; border: 4px solid var(--blue); background: linear-gradient(160deg, #7a5740, #3e2a22); }
  .about-title { right: 533px; top: 662px; font-family: "Montserrat", sans-serif; font-weight: 600; font-size: 12px; color: var(--ink); }
  .about-text { right: 533px; top: 689px; width: 225px; text-align: right; font-size: 6.7px; line-height: 11px; }
  .read-more { right: 533px; top: 762px; font-size: 7px; color: var(--blue); }
  .vline { left: 506px; top: 581px; width: 1px; height: 189px; background: var(--rule); }
  .overview-title { left: 532px; top: 578px; font-family: "Montserrat", sans-serif; font-weight: 600; font-size: 11.5px; color: var(--ink); }
  .overview-text { left: 532px; top: 601px; width: 232px; font-size: 6.7px; line-height: 11px; }
  .overview-text p + p { margin-top: 11px; }
  b { color: var(--ink); font-weight: 600; }

  /* partners */
  .partners { left: 0; top: 826px; width: 1010px; height: 70px; }
  .band-shadow { left: 170px; top: 912px; width: 670px; height: 14px; background: radial-gradient(ellipse at top, rgba(0,0,0,.12), transparent 70%); }

  /* cta */
  .cta { left: 0; top: 942px; width: 1010px; text-align: center; }
  .cta h2 { font-weight: 300; font-size: 24px; color: var(--blue); }
  .cta .intro { font-size: 12px; line-height: 16px; color: #444; margin-top: 6px; }
  .cta .hours { margin-top: 10px; font-size: 8.5px; color: #555; line-height: 15px; }
  .cta .hours strong { font-family: "Montserrat", sans-serif; font-size: 11.5px; color: var(--blue); font-weight: 600; }
  .cta-btn { left: 445px; top: 1074px; width: 120px; height: 31px; background: linear-gradient(90deg, var(--blue-deep), var(--blue)); color: #fff; font-family: "Montserrat", sans-serif; font-weight: 700; font-size: 11.5px; display: flex; align-items: center; justify-content: center; }

  /* footer */
  .copyright { left: 244px; top: 1167px; font-size: 7.5px; color: #555; }
  .footer-nav { left: 444px; top: 1167px; display: flex; font-size: 7.5px; color: #555; }
  .footer-nav span { padding: 0 10px; border-left: 1px solid #999; line-height: 11px; }
  .footer-nav span:first-child { border-left: 0; padding-left: 0; color: var(--blue); }
</style>
</head>
<body>
  <header class="site-header">
    <div class="abs brand">
      <span class="brand-dot"></span>
      <span class="brand-name">Velric Dunmore, PLLC</span>
    </div>
    <nav class="abs main-nav">
      <a class="is-active" style="left:0">Home</a>
      <a style="left:49px">About</a>
      <a style="left:99px">Resources</a>
      <a style="left:166px">Practice Areas</a>
    </nav>
    <div class="abs call-box">
      <div class="q">Any Questions?</div>
      <div class="p">Please Call</div>
      <div class="phone">888-555-0142</div>
    </div>
    <span class="abs or">OR</span>
    <div class="abs email-btn">
      <svg width="10" height="7" viewBox="0 0 10 7"><rect x=".5" y=".5" width="9" height="6" fill="none" stroke="#fff"/><path d="M.5 .5 5 4 9.5 .5" fill="none" stroke="#fff"/></svg>
      Send Email
    </div>
  </header>

  <section class="hero" role="img" aria-label="Warm blurred courtroom photo with brass scales of justice on a wooden desk"></section>
  <h1 class="abs hero-title">Velric Dunmore</h1>
  <div class="abs hero-sub">Paten Law Firm</div>
  <p class="abs hero-text">I am an Intellectual Property Lawyer and focus on patents, copyrights, trademarks, &amp; trade secrets. I work with small businesses and start ups in the chemical and biotech industries.</p>
  <div class="abs contact-btn">
    <small>Need Help?</small>
    <strong>Contact Me</strong>
    <svg width="20" height="20" viewBox="0 0 20 20"><circle cx="10" cy="10" r="9" fill="none" stroke="#fff" stroke-width="1.5"/><path d="M8.5 6 12.5 10 8.5 14" fill="none" stroke="#fff" stroke-width="1.5"/></svg>
  </div>

  <section class="abs info-col" style="left:233px">
    <h3>WHY US?</h3>
    <div class="lead">This is a reason why you choose us</div>
    <p>I am small firm that can provide large-firm service at a reasonable price. I also can charge flat-fees for entreprenuers in certain practice areas.</p>
  </section>
  <section class="abs info-col" style="left:438px">
    <h3>WHAT WE DO</h3>
    <div class="lead">What can we do for you?</div>
    <p>Intellectual Property<span class="sep">I</span>Patents<span class="sep">I</span>Copyrights<br>Trademarks<span class="sep">I</span>Trade secrets<span class="sep">I</span>Healthcare<br>Compliance<span class="sep">I</span>Elder law<span class="sep">I</span>Wills<span class="sep">I</span>Trusts</p>
  </section>
  <section class="abs info-col" style="left:642px">
    <h3>CONTACT INFO</h3>
    <div class="lead">Where you can find us?</div>
    <p>212th ST. Orrick - Mill Park<br>KANSAS - MISSOURI 55819</p>
    <p style="margin-top:8px">Phone. 888-555-0142<br>Email. client@velricdunmore.com</p>
  </section>

  <div class="rule" style="top:537px"></div>

  <div class="abs avatar" role="img" aria-label="Portrait photo of the attorney"></div>
  <h3 class="abs about-title">About Velric</h3>
  <p class="abs about-text"><b>Velric</b> earned a Bachelor's degree in Chemistry from Wexmoor State University where she was a Halvern Science Trust Scholar and went on to receive her Juris Doctorate from Carrowford University. Velric was also a Proctor and Brightline Hale Fellow at Ostrand Law Center, which allowed her to focus her legal studies on Intellectual Property law, including patent....</p>
  <a class="abs read-more">Read more</a>
  <div class="abs vline"></div>
  <h3 class="abs overview-title">Company Overview</h3>
  <div class="abs overview-text">
    <p><b>Velric</b> brings nearly a decade of experience in patent and transactional legal issues to the firm, including client counseling, patent and trademark procurement, technology transfer and licensing in mergers and acquisitions, infringement analysis, validity and freedom-to-operate opinion counseling, patent litigation, and pursuing administrative appeals for patents and trademarks.</p>
    <p>She has worked in a wide variety of technology areas, including chemical/biotechnology, material sciences, fire retardants, pharmaceuticals, computer sciences, automated transaction processes, telecommunications, control systems, wireless operations, mechanical constructions, medical devices, oil and gas technology, pigments and dyes, and semiconductor processes.Is licensed to practice law in both Missouri and Texas and has applied for membership to the North Carolina Bar.</p>
  </div>

  <div class="rule" style="top:800px"></div>

  <svg class="abs partners" viewBox="0 0 1010 70" aria-label="Client badges">
    <circle cx="272" cy="35" r="30" fill="var(--badge)"/>
    <rect x="328" y="26" width="80" height="18" rx="2" fill="var(--badge)"/>
    <circle cx="466" cy="35" r="31" fill="var(--badge)"/>
    <rect x="524" y="7" width="58" height="57" fill="var(--badge)"/>
    <circle cx="632" cy="30" r="29" fill="var(--badge)"/>
    <circle cx="716" cy="32" r="31" fill="var(--badge)"/>
  </svg>
  <div class="abs band-shadow"></div>

  <section class="abs cta">
    <h2>Velric Dunmore - Patent Lawyer.</h2>
    <p class="intro">For business consultation and information of your patents, please contact us.<br>We are ready to serve you.</p>
    <p class="hours">Open <strong>08am - 16pm</strong><br>Appointment <strong>888-555-0142</strong></p>
  </section>
  <div class="abs cta-btn">SEND US EMAIL</div>

  <div class="rule" style="top:1137px"></div>
  <div class="abs copyright">Velric Dunmore I © 2014 All Right Reserved</div>
  <nav class="abs footer-nav">
    <span>Home</span><span>Pricing</span><span>Resource</span><span>Terms &amp; Condition</span><span>Privacy Policy</span><span>Fees</span>
  </nav>
</body>
</html>
```